KLT Company Brochure Design for Consignors

We want to create a company brochure that we can hand out to our potential customers.

We had our staff create one but we didn't like it. I attached it to give you an idea of the contents and texts that should be in there.
This brochure will be a trifold.

The trifold brochure will be handed out to clients and also to clients who have already consigned with us to provide them with information of what happens at auctions and when they're items are sold at auction and contact information of who to call for quesstions.

Target Market(s)

People who have valuables to sell.

Industry/Entity Type

It Company

Requirements
Must have
• It must have our original logo on front with our contact information and a picture of the owner.

```html
<!DOCTYPE html>
<html lang="en">
<head>
<meta charset="utf-8">
<title>KLT Auctioneers – Consignor Trifold</title>
<link href="https://fonts.googleapis.com/css2?family=Cinzel:wght@400;600&family=Crimson+Text&family=Open+Sans:ital,wght@0,400;0,600;0,700;1,400&display=swap" rel="stylesheet">
<style>
  :root{
    --page:#e4e4e4;
    --blue:#1a73c4;
    --blue-deep:#0c58a6;
    --navy:#083a78;
    --gold:#c8a765;
    --gold-light:#e2c98f;
    --gold-dark:#9c7c3f;
    --white:#ffffff;
    --photo-dark:#3f4347;
    --photo-light:#b9b9b9;
  }
  *{box-sizing:border-box;margin:0;padding:0}
  html,body{width:1200px;height:800px;overflow:hidden}
  body{background:var(--page);font-family:"Open Sans",Arial,sans-serif;color:var(--white)}
  .brochure{position:absolute;left:60px;top:20px;width:1080px;height:760px;display:flex;box-shadow:0 6px 18px rgba(0,0,0,.18)}
  .panel{position:relative;width:360px;height:760px;overflow:hidden;
    background:linear-gradient(180deg,var(--blue) 0%,var(--blue-deep) 100%)}
  .panel + .panel{border-left:1px solid rgba(0,0,0,.12)}
  .panel svg.art{position:absolute;left:0;top:0}

  /* brand lockup */
  .brand{position:absolute;left:0;right:0;text-align:center}
  .brand-mark{display:inline-flex;align-items:center;gap:10px;font-family:"Cinzel",serif;font-weight:600;font-size:19px;letter-spacing:1px;color:var(--white)}
  .brand-square{width:30px;height:30px;background:var(--white)}
  .brand-sub{font-size:7px;letter-spacing:1.5px;margin-top:4px;text-transform:uppercase}
  .rule{position:absolute;height:1px;background:var(--gold)}

  /* panel one */
  .tagline{position:absolute;left:40px;right:40px;top:175px;font-size:15px;line-height:24px;color:var(--gold-light);letter-spacing:.3px;text-align:center}
  .contact-title{position:absolute;left:0;right:0;top:330px;text-align:center;font-family:"Cinzel",serif;font-size:18px;letter-spacing:2px;color:var(--gold-light)}
  .contact-list{position:absolute;left:0;right:0;top:370px;text-align:center;list-style:none;font-size:14px;line-height:22px}
  .band-gold{position:absolute;left:0;right:0;background:linear-gradient(180deg,var(--gold-light),var(--gold))}
  .photo{position:absolute;left:0;right:0}

  /* panel two */
  .process-title{position:absolute;left:0;right:0;top:34px;text-align:center;font-family:"Cinzel",serif;font-size:17px;line-height:22px;letter-spacing:.5px}
  .steps{position:absolute;left:28px;right:28px;top:108px;font-size:9.2px;line-height:13px}
  .step-head{font-family:"Cinzel",serif;font-weight:600;font-size:12px;color:var(--gold-light);margin:0 0 4px}
  .step{margin-bottom:14px}
  .step p{margin-bottom:6px}
  .step strong{font-weight:700}
  .gold-text{color:var(--gold-light);font-weight:600}
  .accountant{position:absolute;right:26px;top:622px;width:200px;text-align:right}
  .accountant-note{font-size:9.5px;line-height:13px;font-style:italic;color:var(--gold-light);margin-bottom:8px}
  .accountant-list{list-style:none;font-size:13px;line-height:18px}

  /* panel three */
  .owner{position:absolute;left:0;right:0;top:160px;text-align:center;font-family:"Crimson Text",serif;font-size:22px;line-height:28px}
  .partner{position:absolute;left:70px;right:0;top:574px;text-align:center;font-family:"Cinzel",serif;font-size:14px;letter-spacing:1.5px;color:var(--white)}
  .partner-sub{display:block;font-size:7px;letter-spacing:4px}
</style>
</head>
<body>
<main class="brochure">

  <!-- Panel: contact -->
  <section class="panel panel-contact">
    <div class="brand" style="top:48px">
      <div class="brand-mark"><span class="brand-square"></span>KLT AUCTIONEERS</div>
      <div class="brand-sub">Real Estate · Auctions · Appraisals</div>
    </div>
    <div class="rule" style="left:40px;right:40px;top:160px"></div>
    <p class="tagline">Your market leader and trendsetter for bringing world wide customer demand for your elite real estate, fine art, collectibles and all your objects of enduring value.</p>
    <div class="rule" style="left:40px;right:40px;top:300px"></div>
    <h2 class="contact-title">CONTACT US</h2>
    <ul class="contact-list">
      <li>555-210-4400</li>
      <li>PO Box 48120</li>
      <li>Maple Grove, CA 95000</li>
      <li>www.kltauctions.com</li>
      <li>www.kltauctioneers.com</li>
      <li>appraisals@kltauctions.com</li>
    </ul>
    <div class="band-gold" style="top:560px;height:22px"></div>
    <div class="photo" style="top:582px;height:178px;background:linear-gradient(120deg,var(--photo-light) 0%,#8a8a8a 45%,var(--photo-dark) 100%)" role="img" aria-label="Black and white photo of a woman examining antique toy figures"></div>
  </section>

  <!-- Panel: consignment process -->
  <section class="panel panel-process">
    <h2 class="process-title">OUR CONSIGNMENT PROCESS<br>EASY AS 1, 2, 3!</h2>
    <div class="rule" style="left:60px;right:60px;top:90px"></div>
    <div class="steps">
      <div class="step">
        <h3 class="step-head">STEP #1</h3>
        <p>The process starts with a free evaluation of your item or collection by one of our appraisers, either in person or based on pictures. For an in-person evaluation with one of our specialists, we provide a weekly walk-in appraisal day at both of our Maple Grove and Seacliff locations.</p>
        <p><strong>Maple Grove walk-in appraisal day:</strong><br>Every Wednesday between 11am to 1pm.<br>Seacliff walk in appraisal day:<br>Every Thursday between 11am to 1pm.</p>
        <p><strong>To send images:</strong><br>Email images, along with the dimensions of the piece, and any other helpful information (signatures, marks, condition, medium) to <span class="gold-text">appraisals@kltauctions.com</span>. If you prefer to mail us photos, please send them to our office at: <span class="gold-text">KLT Auctioneers, Inc. PO Box 48120 Maple Grove, CA 95000</span></p>
      </div>
      <div class="step">
        <h3 class="step-head">STEP #2</h3>
        <p>After your items arrive in our offices, our in-house photography department will photograph them for our online and print catalogues, live auction websites, advertisements and brochures. We catalogue each item with full descriptions, condition reports and estimates. Once your items are catalogued, a Consignor Order Report will be emailed to you for your confirmation.</p>
      </div>
      <div class="step">
        <h3 class="step-head">STEP #3</h3>
        <p>After the auction, a Pending Consignor Settlement Report will be emailed to you one week after the auction. Due to after auction sales that may occur for any unsold items and pending collection from online winning bidders, once payment from the winning bidders have been collected for your items and the items are received in satisfaction, your consignor proceeds check will be released.</p>
      </div>
    </div>
    <svg class="art" width="360" height="760" viewBox="0 0 360 760" aria-hidden="true">
      <path d="M0 640 C90 600 170 610 240 700 C270 735 300 755 330 760 L0 760Z" fill="var(--gold)"/>
      <path d="M0 652 C90 614 165 625 230 710 C258 740 285 758 305 760 L0 760Z" fill="var(--blue-deep)"/>
    </svg>
    <svg class="art" width="360" height="760" viewBox="0 0 360 760">
      <circle cx="70" cy="640" r="50" fill="var(--gold)"/>
      <circle cx="70" cy="640" r="45" fill="url(#portraitTone)" role="img" aria-label="Portrait of the accountant"/>
      <defs>
        <radialGradient id="portraitTone" cx="50%" cy="40%" r="60%">
          <stop offset="0" stop-color="#c99a86"/>
          <stop offset="1" stop-color="#5a2a25"/>
        </radialGradient>
      </defs>
    </svg>
    <div class="accountant">
      <p class="accountant-note">For any questions regarding your post auction proceeds payment, please contact our accountant at:</p>
      <ul class="accountant-list">
        <li>Marisa Dunn</li>
        <li>555-380-7120</li>
        <li>marisa@kltauctions.com</li>
        <li>www.kltauctions.com</li>
      </ul>
    </div>
  </section>

  <!-- Panel: cover -->
  <section class="panel panel-cover">
    <div class="brand" style="top:48px">
      <div class="brand-mark"><span class="brand-square"></span>KLT AUCTIONEERS</div>
      <div class="brand-sub">Real Estate · Auctions · Appraisals</div>
    </div>
    <div class="rule" style="left:30px;right:30px;top:135px"></div>
    <h1 class="owner">Kevin L. Talbot<br>Owner and CEO</h1>
    <svg class="art" width="360" height="760" viewBox="0 0 360 760">
      <defs>
        <linearGradient id="ownerTone" x1="0" y1="0" x2="1" y2="1">
          <stop offset="0" stop-color="#6b6f74"/>
          <stop offset="0.5" stop-color="#9a9a96"/>
          <stop offset="1" stop-color="var(--photo-dark)"/>
        </linearGradient>
      </defs>
      <path d="M360 228 C255 232 165 262 128 318 C94 372 86 462 112 560 L360 560Z" fill="url(#ownerTone)" role="img" aria-label="Photo of the owner in a grey suit holding his award plaques"/>
      <path d="M360 212 C250 216 150 250 112 310 C74 372 66 462 92 560 L112 560 C86 462 94 372 128 318 C165 262 255 232 360 228Z" fill="var(--gold)"/>
      <rect x="150" y="470" width="40" height="55" rx="3" fill="#1c2f6a"/>
      <rect x="195" y="465" width="40" height="60" rx="3" fill="#203a7c"/>
      <rect x="240" y="460" width="40" height="65" rx="3" fill="#1c2f6a"/>
      <path d="M0 560 L360 560 L360 610 L40 610 C20 610 8 595 0 580Z" fill="var(--gold)"/>
      <rect x="80" y="572" width="26" height="26" fill="none" stroke="var(--white)" stroke-width="1.5"/>
    </svg>
    <div class="partner">HARBOR CREST<span class="partner-sub">REAL ESTATE</span></div>
  </section>

</main>
</body>
</html>
```